Verdant Holdings SA Business Cards

Dear all,
Thank you for reading my brief and project. My company is doing doing advisory in real estate and to comapnies + real estates services as asset management, brokerage, development etc.
I would like to get a business card for my company which is clear, professionnal and serious.
Please have a look to the attachement to see the logos of the company

Industry/Entity Type

Real Estate

Contact Information for Business Card

I would like to have in the business card the following
Principal side:
- Logo of the company (or Monogram)
- First and Last Name (Marcel Tobler)
- Mobile number
- email address

Second side:
- Address (Chemin des Vergers 17, 1292 Chambésy - Switzerland)
- website (www.verdantholdings.ch)

Requirements
Must have
• Refer to the typeface and logo colors

```html
<!DOCTYPE html>
<html lang="en">
<head>
<meta charset="utf-8">
<title>Verdant Holdings SA – Business Cards</title>
<link href="https://fonts.googleapis.com/css2?family=Montserrat:wght@500&family=Roboto:wght@400;500;700&display=swap" rel="stylesheet">
<style>
  :root {
    --backdrop: #dcdcdc;
    --paper: #ffffff;
    --brand-blue: #0a80c6;
    --brand-blue-deep: #0677bf;
    --name-blue: #1476c0;
    --ink-dark: #4a5461;
    --ink-text: #3f4650;
    --rule: #8a8f96;
  }
  * { margin: 0; padding: 0; box-sizing: border-box; }
  html, body { width: 1200px; height: 1200px; overflow: hidden; }
  body { background: var(--backdrop); position: relative; font-family: "Roboto", Arial, sans-serif; }

  .card {
    position: absolute;
    left: 262px;
    width: 800px;
    height: 457px;
    transform: scale(0.8575);
    transform-origin: top left;
  }
  .card--front { top: 165px; background: var(--paper); }
  .card--back { top: 653px; background: linear-gradient(180deg, var(--brand-blue) 0%, var(--brand-blue-deep) 100%); }

  /* Front */
  .brand-lockup {
    position: absolute;
    top: 50px;
    right: 53px;
    height: 105px;
    display: flex;
    align-items: center;
  }
  .brand-square { width: 40px; height: 40px; background: var(--brand-blue); }
  .brand-divider { width: 1px; height: 105px; background: var(--brand-blue); margin: 0 30px 0 32px; }
  .brand-name {
    font-family: "Montserrat", Arial, sans-serif;
    font-weight: 500;
    font-size: 25px;
    color: var(--ink-dark);
    letter-spacing: 0.2px;
  }

  .holder { position: absolute; left: 55px; top: 283px; }
  .holder-name { font-weight: 700; font-size: 30px; color: var(--name-blue); line-height: 1.1; }
  .holder-title { font-weight: 500; font-size: 20px; color: var(--ink-text); line-height: 1.2; }

  .contact-rule { position: absolute; left: 59px; right: 58px; top: 353px; height: 2px; background: var(--rule); }

  .contact-list { position: absolute; left: 55px; top: 372px; list-style: none; }
  .contact-item { display: flex; align-items: center; font-size: 19px; color: var(--ink-text); height: 24px; }
  .contact-item svg { width: 16px; margin-right: 11px; }

  .front-web { position: absolute; right: 52px; top: 391px; font-size: 19px; color: var(--ink-text); }

  .edge-line { position: absolute; left: 0; right: 0; top: 442px; height: 3px; background: var(--ink-dark); }
  .edge-band { position: absolute; left: 0; right: 0; top: 447px; height: 10px; background: var(--brand-blue); }

  /* Back */
  .back-lockup { position: absolute; right: 70px; top: 340px; text-align: right; color: #fff; }
  .back-name { font-family: "Montserrat", Arial, sans-serif; font-weight: 500; font-size: 40px; line-height: 1.1; }
  .back-web { font-size: 18px; letter-spacing: 0.52em; margin-right: -0.52em; margin-top: 4px; }
</style>
</head>
<body>
  <section class="card card--front" aria-label="Business card front">
    <div class="brand-lockup">
      <div class="brand-square"></div>
      <div class="brand-divider"></div>
      <div class="brand-name">VERDANT HOLDINGS</div>
    </div>

    <div class="holder">
      <p class="holder-name">Marcel Tobler</p>
      <p class="holder-title">President</p>
    </div>

    <div class="contact-rule"></div>

    <ul class="contact-list">
      <li class="contact-item">
        <svg viewBox="0 0 16 22" height="22" aria-hidden="true"><rect x="2" y="1" width="12" height="20" rx="2" fill="none" stroke="#1476c0" stroke-width="2"/><rect x="5" y="4" width="6" height="11" fill="#1476c0"/></svg>
        412-708-5531
      </li>
      <li class="contact-item">
        <svg viewBox="0 0 16 12" height="12" aria-hidden="true"><rect x="0.5" y="0.5" width="15" height="11" fill="#1476c0"/><path d="M1 1 L8 7 L15 1" fill="none" stroke="#fff" stroke-width="1.3"/></svg>
        info@verdantholdings.ch
      </li>
    </ul>

    <p class="front-web">www.verdantholdings.ch</p>

    <div class="edge-line"></div>
    <div class="edge-band"></div>
  </section>

  <section class="card card--back" aria-label="Business card back">
    <div class="back-lockup">
      <p class="back-name">VERDANT HOLDINGS</p>
      <p class="back-web">www.verdantholdings.ch</p>
    </div>
  </section>
</body>
</html>
```